Webbanner-Design für Verkäufer von versilberten Wohnaccessoires
Zielgruppe
Wir verkaufen versilberte Wohnaccessoires (Luxus)
www.morvani-casa.de
Aufgabenstellung
Wir sind auf der Suche nach drie Bannern die bei uns auf der Webseite durchlaufen (www.morvani-casa.de)
1. Banner:
Schriftzug: Deko-Highlights für das perfekte Dinner
3x Buttons: GLÄSER / LEUCHTER / KARAFFEN
2. Banner: Die Teelichterkerze - Entdecke die genial Idee
2x Buttons: Kerze mit Ø 8cm / Kerze mit Ø 10cm
3. Banner: Die gemütlichste Dekoration zu Weihnachten
3x Buttons: Teelichter / Adventskränze / Dekoration
4. Banner: Glänzende Bilderrahmen - das perfekte Geschenk!
3x Buttons: 10x15cm / 13x18cm / 15x20cm

```html
<!DOCTYPE html>
<html lang="de">
<head>
<meta charset="utf-8">
<title>Morvani Casa – Deko-Highlights</title>
<link rel="stylesheet" href="https://fonts.googleapis.com/css2?family=Open+Sans:wght@400;600;700&family=Arimo:wght@700&display=swap">
<style>
:root{
  --ink:#1b1b1b;
  --text:#333;
  --band:#1d1d1d;
  --white:#fff;
  --btn-grey:#e6e6e6;
  --chip:rgba(232,232,232,.72);
  --chip-text:#3a3a3a;
}
*{box-sizing:border-box;margin:0;padding:0}
html,body{width:1200px;height:947px;overflow:hidden;background:var(--white)}
body{position:relative;font-family:"Open Sans",sans-serif;color:var(--text)}
.abs{position:absolute}
.cookie-note{left:80px;top:20px;font-size:11.3px;color:var(--ink)}
.cookie-accept{left:1026px;top:10px;width:104px;height:36px;background:var(--ink);color:var(--white);font-size:11.5px;font-weight:700;display:flex;align-items:center;justify-content:center}
.brand{left:80px;top:78px;font-size:34px;font-weight:400;letter-spacing:2px;color:var(--ink);line-height:1}
.utility-nav{top:64px;font-size:12px;color:var(--text);display:flex;align-items:center;gap:4px}
.cart{left:1010px;top:55px;width:112px;height:33px;background:var(--btn-grey);font-size:12px;font-weight:600;display:flex;align-items:center;justify-content:center;gap:6px;color:var(--ink)}
.main-nav{left:393px;top:105px;display:flex;align-items:center;gap:13px;font-size:13.4px;color:var(--ink)}
.usp-band{left:0;top:140px;width:1200px;height:33px;background:var(--band);color:var(--white);font-size:11.5px}
.usp{top:9px;display:flex;align-items:center;gap:8px}
.hero{left:79px;top:173px;width:1043px;height:382px;overflow:hidden;
  background:
    radial-gradient(ellipse 18% 30% at 15% 12%,rgba(200,140,130,.55),transparent 70%),
    radial-gradient(ellipse 22% 22% at 16% 62%,rgba(90,20,25,.7),transparent 70%),
    radial-gradient(ellipse 30% 25% at 60% 78%,rgba(235,235,235,.55),transparent 70%),
    radial-gradient(ellipse 25% 40% at 85% 30%,rgba(30,25,22,.8),transparent 70%),
    linear-gradient(160deg,#5a4236 0%,#3a2d26 40%,#6b5546 70%,#8c7b6e 100%)}
.hero-title{right:21px;top:52px;text-align:right;font-family:"Arimo",sans-serif;font-weight:700;color:var(--white);font-size:31px;line-height:39px;letter-spacing:.5px;text-shadow:0 1px 3px rgba(0,0,0,.35)}
.hero-chip{height:47px;background:var(--chip);color:var(--chip-text);font-family:"Arimo",sans-serif;font-weight:700;font-size:17px;letter-spacing:.5px;display:flex;align-items:center;justify-content:center;gap:6px}
.tile{top:573px;width:246px;height:312px}
.tile-bar{background:radial-gradient(ellipse 50% 30% at 70% 75%,rgba(190,200,90,.6),transparent 70%),linear-gradient(170deg,#a9a49a,#d8d2c2 45%,#c9bb95 75%,#a8a08a)}
.tile-table{background:radial-gradient(ellipse 40% 20% at 40% 30%,rgba(220,150,70,.55),transparent 70%),linear-gradient(175deg,#eae6e0 0%,#dcd6cf 35%,#f2f1ef 55%,#8a6448 100%)}
.tile-frames{background:radial-gradient(ellipse 30% 20% at 20% 30%,rgba(110,150,60,.55),transparent 70%),linear-gradient(170deg,#e3d9ca,#c6b49a 50%,#8b6a4c 100%)}
.tile-candles{background:radial-gradient(ellipse 35% 30% at 50% 75%,rgba(200,200,205,.7),transparent 70%),linear-gradient(175deg,#ececea,#d4d3d2 55%,#55585e 100%)}
</style>
</head>
<body>
<p class="abs cookie-note">Diese Website verwendet Cookies, um Ihnen die bestmögliche Funktionalität bieten zu können.</p>
<div class="abs cookie-accept">Einverstanden</div>

<div class="abs brand">MORVANI</div>

<div class="abs utility-nav" style="left:718px">
  <svg width="11" height="11" viewBox="0 0 12 12"><circle cx="5" cy="5" r="3.6" fill="none" stroke="#222" stroke-width="1.6"/><path d="M7.6 7.6 11 11" stroke="#222" stroke-width="1.8"/></svg>Suchen</div>
<div class="abs utility-nav" style="left:799px">Service/Hilfe <svg width="9" height="6" viewBox="0 0 9 6"><path d="M1 1l3.5 3.5L8 1" fill="none" stroke="#333" stroke-width="1.4"/></svg></div>
<div class="abs utility-nav" style="left:908px">Mein Konto <svg width="9" height="6" viewBox="0 0 9 6"><path d="M1 1l3.5 3.5L8 1" fill="none" stroke="#333" stroke-width="1.4"/></svg></div>
<div class="abs cart"><svg width="14" height="12" viewBox="0 0 14 12"><path d="M0 1h2.5l2 7h7l2-5.5H4" fill="none" stroke="#222" stroke-width="1.6"/><circle cx="5.5" cy="10.5" r="1.2" fill="#222"/><circle cx="10.5" cy="10.5" r="1.2" fill="#222"/></svg>Warenkorb</div>

<nav class="abs main-nav">
  <svg width="13" height="12" viewBox="0 0 13 12"><path d="M6.5 0 0 6h2v6h3.5V8h2v4H11V6h2z" fill="#222"/></svg>
  <span>Geschenke</span><span>NEU</span><span>Material</span><span>Bar</span><span>Tafel</span><span>Wohnen</span><span>Accessoires</span><span>Kinder</span><span>Lurena Porzellan</span><span>Weihnachten</span><span>SALE</span>
</nav>

<div class="abs usp-band">
  <div class="abs usp" style="left:106px"><svg width="14" height="9" viewBox="0 0 14 9"><path d="M0 1h8v5h6V4l-2-2H9" fill="#fff"/><rect x="0" y="1" width="9" height="5" fill="#fff"/><circle cx="3" cy="7.5" r="1.3" fill="#fff"/><circle cx="11" cy="7.5" r="1.3" fill="#fff"/></svg>Kostenloser Versand ab € 20,- Bestellwert</div>
  <div class="abs usp" style="left:428px"><svg width="12" height="12" viewBox="0 0 12 12"><circle cx="6" cy="6" r="5" fill="none" stroke="#fff" stroke-width="1.4"/><path d="M6 3v3.3l2 1.2" fill="none" stroke="#fff" stroke-width="1.3"/></svg>Versand innerhalb von 48h*</div>
  <div class="abs usp" style="left:676px"><svg width="12" height="12" viewBox="0 0 12 12"><rect x="0" y="5" width="3" height="7" fill="#fff"/><path d="M4 5l3-5c1.5 0 1.5 1.5 1 3h3.5l-1 9H4z" fill="#fff"/></svg>30 Tage Geld-Zurück-Garantie</div>
  <div class="abs usp" style="left:931px"><svg width="11" height="11" viewBox="0 0 12 12"><path d="M2 0l2.5 3-1.5 1.5c.8 1.8 2.2 3.2 4 4L8.5 7 12 9.5 10.5 12C5 11.5.5 7 0 1.5z" fill="#fff"/></svg>24h Hotline 0421 - 58 92 304</div>
</div>

<section class="abs hero" role="img" aria-label="Gedeckter Dinnertisch mit Rotweinkaraffe, Silberleuchter und Weingläsern">
  <h1 class="abs hero-title">DEKO-HIGHLIGHTS<br>für das perfekte Dinner</h1>
  <div class="abs hero-chip" style="left:150px;top:85px;width:152px">KARAFFEN <span>›</span></div>
  <div class="abs hero-chip" style="left:306px;top:160px;width:154px">LEUCHTER <span>›</span></div>
  <div class="abs hero-chip" style="left:549px;top:178px;width:153px">GLÄSER <span>›</span></div>
</section>

<div class="abs tile tile-bar" style="left:80px" role="img" aria-label="Silberbecher mit Gin Tonic, Limetten und Zitronen auf einem Silbertablett"></div>
<div class="abs tile tile-table" style="left:345px" role="img" aria-label="Frühstückstisch mit Serviettenring und Eierbecher"></div>
<div class="abs tile tile-frames" style="left:610px" role="img" aria-label="Silberne Bilderrahmen, Vase mit Blumen und Teelichthalter auf einem Koffer"></div>
<div class="abs tile tile-candles" style="left:875px" role="img" aria-label="Gehämmerte Silberleuchter mit weißen Kerzen auf einem Spiegeltablett"></div>
</body>
</html>
```